Bright Ink Business Card

This is a business card for a printing company but I actually don't have a logo. Just need to typeset the words "Bright Ink Printing" as the logo. Then add my name "Margot Vell" + phone number + address

Target Market(s)

ceos and professionals

Industry/Entity Type

printing and manufacturing

Contact Information for Business Card

Bright Ink Printing/ 4817 calloway ave. S. El Monte, CA 91548/ 626-739-2048/ Margot Vell

Font styles to use
Serif
Other font styles liked:
• a modern font would be nice

Colors
0054AA
0677BA
7BADD7
CADEEF
E8F1F8
0094D4
00A9DD
6FCCEA
C7EBF8
E9F6FB

Requirements
Must have
• company name, number, address
Nice to have
• nice bold feel
Should not have
• nothing in particular

```html
<!DOCTYPE html>
<html lang="en">
<head>
<meta charset="utf-8">
<title>Bright Ink Printing — Business Card</title>
<link rel="stylesheet" href="https://fonts.googleapis.com/css2?family=Arimo:wght@400;700&display=swap">
<style>
  :root {
    --backdrop: #9a9a9a;
    --card: #f4f4f4;
    --brand-blue: #0677ba;
    --deep-blue: #0054aa;
    --ink-grey: #5a5a5a;
    --rule-blue: #3a8fd6;
  }
  * { box-sizing: border-box; margin: 0; padding: 0; }
  html, body {
    width: 1200px;
    height: 1050px;
    overflow: hidden;
  }
  body {
    background: var(--backdrop);
    font-family: "Arimo", Arial, sans-serif;
    position: relative;
  }
  .card {
    position: absolute;
    width: 640px;
    height: 366px;
    background: var(--card);
    box-shadow: 0 10px 30px rgba(0, 0, 0, 0.28);
  }
  .card--front { left: 110px; top: 110px; }
  .card--back  { left: 450px; top: 570px; }

  /* Front */
  .front-brand {
    position: absolute;
    left: 60px;
    top: 150px;
    width: 220px;
    color: var(--brand-blue);
    font-weight: 700;
    font-size: 27px;
    line-height: 1.15;
  }
  .front-divider {
    position: absolute;
    left: 312px;
    top: 110px;
    width: 2px;
    height: 150px;
    background: var(--rule-blue);
  }
  .contact {
    position: absolute;
    left: 340px;
    top: 112px;
    color: var(--ink-grey);
    font-size: 13.5px;
    line-height: 1.3;
  }
  .contact__name {
    color: var(--brand-blue);
    font-weight: 700;
    font-size: 20px;
    line-height: 1.1;
  }
  .contact__title { margin-bottom: 12px; }
  .contact__address { margin-bottom: 12px; }

  /* Back */
  .back-brand {
    position: absolute;
    left: 0;
    right: 0;
    top: 0;
    bottom: 0;
    display: flex;
    align-items: center;
    justify-content: center;
    color: var(--deep-blue);
    font-weight: 700;
    font-size: 52px;
  }
</style>
</head>
<body>
  <section class="card card--front" aria-label="Business card front">
    <div class="front-brand">Bright Ink Printing</div>
    <div class="front-divider"></div>
    <div class="contact">
      <p class="contact__name">Margot Vell</p>
      <p class="contact__title">President</p>
      <p class="contact__address">4817 Calloway Ave.<br>S. El Monte, CA 91548</p>
      <p>p. 626-739-2048</p>
      <p>e. info@brightinkprinting.com</p>
      <p>w. www.brightinkprinting.com</p>
    </div>
  </section>

  <section class="card card--back" aria-label="Business card back">
    <div class="back-brand">Bright Ink Printing</div>
  </section>
</body>
</html>
```